Creative, Colorful, Dynamic Infographic for Global Non-Profit

We are a global arts and education non-profit in need of an infographic that illustrates four key skills embedded in our work: Curiosity, Listening, Imagination, Postive Action.
We work primarily with educators, students, and artists who use the power of personal stories to build community and connection and to bridge divides.
Our new brand guidelines, logos, and fonts are here: https://stylekit.example/quillbridge-7
I've attached a mock-up of the graphic and the required text. (Note the attached design was created by a staff person, your final design does not need to be the same. The color scheme and text of the final design should match the brand guidelines above.)
The graphic will be used for both web and print media and should include the purple Quillbridge 7 logo (also attached).
Ideally the final design will delight audiences and spark interest in our work.

```html
<!DOCTYPE html>
<html lang="en">
<head>
<meta charset="utf-8">
<title>Quillbridge 7 – Four Skills</title>
<link rel="stylesheet" href="https://fonts.googleapis.com/css2?family=Arimo:wght@400;700&display=swap">
<style>
  :root {
    --purple: #66348f;
    --purple-edge: #7b4b9c;
    --white: #ffffff;
    --ink: #1a1a1a;
    --faint: #dcd2e4;

    --teal-face: #9ad6c8;
    --teal-mid: #7fb3a8;
    --teal-edge: #5f8a80;
    --teal-head: #2e4a44;

    --gold-face: #fbc97a;
    --gold-mid: #d9a85c;
    --gold-edge: #a57d45;
    --gold-head: #5a4220;

    --coral-face: #f9bfa0;
    --coral-mid: #f39a8c;
    --coral-edge: #e47f72;
    --coral-head: #7a3e36;

    --lilac-face: #d6c0d8;
    --lilac-mid: #b7a2b8;
    --lilac-edge: #7e6e7c;
    --lilac-head: #3a2d38;
  }
  html, body {
    margin: 0;
    padding: 0;
    width: 1200px;
    height: 849px;
    overflow: hidden;
    background: var(--white);
  }
  .skills-cycle {
    display: block;
    width: 1200px;
    height: 849px;
    font-family: "Arimo", Arial, sans-serif;
  }
  .card-title { fill: var(--white); font-weight: 700; font-size: 22px; text-anchor: middle; }
  .card-body { fill: var(--ink); font-size: 18.5px; text-anchor: middle; }
  .arrow-text { fill: var(--ink); font-size: 14px; text-anchor: middle; }
  .arrow-outline { stroke: var(--white); stroke-width: 6; stroke-linejoin: round; }
  .brand-name { fill: var(--white); font-size: 16px; font-weight: 700; text-anchor: middle; }
  .brand-footer { fill: var(--faint); font-size: 16px; font-weight: 700; letter-spacing: 1px; text-anchor: middle; }
</style>
</head>
<body>
<svg class="skills-cycle" viewBox="0 0 842 596" xmlns="http://www.w3.org/2000/svg" role="img" aria-label="Four skills cycle: Curiosity, Listening, Imagination, Positive Action">
  <defs>
    <linearGradient id="frame-fade" x1="0" y1="0" x2="0" y2="1">
      <stop offset="0" stop-color="var(--purple-edge)"/>
      <stop offset="0.06" stop-color="#ffffff"/>
      <stop offset="0.9" stop-color="#ffffff"/>
      <stop offset="1" stop-color="var(--purple-edge)"/>
    </linearGradient>
  </defs>

  <rect class="backdrop" x="0" y="0" width="842" height="596" fill="url(#frame-fade)"/>

  <!-- Curiosity card -->
  <g class="card card--curiosity">
    <rect x="42" y="52" width="288" height="190" rx="24" fill="var(--teal-edge)"/>
    <rect x="42" y="58" width="288" height="176" rx="22" fill="var(--teal-mid)"/>
    <rect x="42" y="64" width="288" height="160" rx="20" fill="var(--teal-face)"/>
    <path d="M42 86 Q42 64 64 64 L308 64 Q330 64 330 86 L330 102 L42 102 Z" fill="var(--teal-head)"/>
    <text class="card-title" x="183" y="90">Curiosity</text>
    <text class="card-body" x="183" y="126">Focus on how</text>
    <text class="card-body" x="183" y="152">you can learn from</text>
    <text class="card-body" x="183" y="176">another’s knowledge and</text>
    <text class="card-body" x="183" y="200">experience.</text>
  </g>

  <!-- Positive Action card -->
  <g class="card card--action">
    <rect x="515" y="52" width="287" height="190" rx="24" fill="var(--gold-edge)"/>
    <rect x="515" y="58" width="287" height="176" rx="22" fill="var(--gold-mid)"/>
    <rect x="515" y="64" width="287" height="160" rx="20" fill="var(--gold-face)"/>
    <path d="M515 86 Q515 64 537 64 L780 64 Q802 64 802 86 L802 102 L515 102 Z" fill="var(--gold-head)"/>
    <text class="card-title" x="658" y="90">Positive Action</text>
    <text class="card-body" x="658" y="142">Show that your words</text>
    <text class="card-body" x="658" y="167">and actions matter</text>
  </g>

  <!-- Listening card -->
  <g class="card card--listening">
    <rect x="42" y="350" width="288" height="196" rx="24" fill="var(--coral-edge)"/>
    <rect x="42" y="356" width="288" height="182" rx="22" fill="var(--coral-mid)"/>
    <rect x="42" y="362" width="288" height="166" rx="20" fill="var(--coral-face)"/>
    <path d="M42 384 Q42 362 64 362 L308 362 Q330 362 330 384 L330 404 L42 404 Z" fill="var(--coral-head)"/>
    <text class="card-title" x="183" y="391">Listening</text>
    <text class="card-body" x="183" y="448">Seek to understand</text>
    <text class="card-body" x="183" y="473">before speaking</text>
  </g>

  <!-- Imagination card -->
  <g class="card card--imagination">
    <rect x="515" y="350" width="287" height="196" rx="24" fill="var(--lilac-edge)"/>
    <rect x="515" y="356" width="287" height="182" rx="22" fill="var(--lilac-mid)"/>
    <rect x="515" y="362" width="287" height="166" rx="20" fill="var(--lilac-face)"/>
    <path d="M515 384 Q515 362 537 362 L780 362 Q802 362 802 384 L802 404 L515 404 Z" fill="var(--lilac-head)"/>
    <text class="card-title" x="658" y="391">Imagination</text>
    <text class="card-body" x="658" y="446">Consider possibilities</text>
    <text class="card-body" x="658" y="471">beyond what you know</text>
  </g>

  <!-- Connector: Positive Action to Curiosity -->
  <g class="connector connector--left">
    <polygon class="arrow-outline" points="302,145 348,90 348,106 522,106 522,186 348,186 348,200" fill="var(--gold-face)"/>
    <text class="arrow-text" x="438" y="126">Your positive actions</text>
    <text class="arrow-text" x="438" y="146">lead to curiosity about</text>
    <text class="arrow-text" x="438" y="166">what else is possible</text>
  </g>

  <!-- Connector: Curiosity to Listening -->
  <g class="connector connector--down">
    <polygon points="135,222 235,222 235,285 270,285 183,354 95,285 135,285" fill="var(--teal-face)"/>
    <text class="arrow-text" x="184" y="248">Your</text>
    <text class="arrow-text" x="184" y="268">curiosity</text>
    <text class="arrow-text" x="184" y="288">allows</text>
    <text class="arrow-text" x="184" y="308">you to</text>
    <text class="arrow-text" x="184" y="328">listen</text>
  </g>

  <!-- Connector: Listening to Imagination -->
  <g class="connector connector--right">
    <polygon points="322,412 474,412 474,386 536,456 474,526 474,500 322,500" fill="var(--coral-face)"/>
    <text class="arrow-text" x="414" y="438">Your listening allows</text>
    <text class="arrow-text" x="414" y="458">you to take in new</text>
    <text class="arrow-text" x="414" y="478">information</text>
  </g>

  <!-- Connector: Imagination to Positive Action -->
  <g class="connector connector--up">
    <polygon points="662,224 756,298 712,298 712,360 612,360 612,298 568,298" fill="var(--lilac-face)"/>
    <text class="arrow-text" x="662" y="264">Your</text>
    <text class="arrow-text" x="662" y="284">imagination</text>
    <text class="arrow-text" x="662" y="304">can spark</text>
    <text class="arrow-text" x="662" y="324">positive</text>
    <text class="arrow-text" x="662" y="344">action</text>
  </g>

  <!-- Brand mark -->
  <g class="brand">
    <circle cx="424" cy="285" r="68" fill="var(--purple)"/>
    <text class="brand-name" x="424" y="291">Quillbridge 7</text>
  </g>

  <text class="brand-footer" x="424" y="554">QUILLBRIDGE 7</text>
</svg>
</body>
</html>
```